Catalogue Design Project

Hi all,

I would like to design Catalogue for our Range Hood products. I am looking for help to design a elegant catalogue impress our potential customer.

Thanks,

Marek

Target Market(s)

Our customers are in US, Canada as well as Australia.

Requirements
Must have
• Please used the pictures of range hood models from the attached file (6 models.rar). Our company information.

Nice to have
• It is nice if the cataloge design as a book style.

```html
<!DOCTYPE html>
<html lang="en">
<head>
<meta charset="utf-8">
<title>RangeHood Series – Contents</title>
<link rel="stylesheet" href="https://fonts.googleapis.com/css2?family=Ubuntu:ital,wght@0,400;0,500;0,700;1,400&family=Ubuntu+Condensed&display=swap">
<style>
  :root {
    --ink: #111111;
    --red: #e0101a;
    --panel: #c6c7c9;
    --white: #ffffff;
    --rule-dark: #222222;
    --thumb-top: #ffffff;
    --thumb-bottom: #d9f1df;
  }
  * { margin: 0; padding: 0; box-sizing: border-box; }
  html, body { width: 1200px; height: 846px; overflow: hidden; background: var(--white); }
  body { font-family: "Ubuntu", sans-serif; color: var(--ink); }
  .page { position: relative; width: 1200px; height: 846px; }

  .section-title { position: absolute; left: 55px; top: 34px; font-size: 25px; font-weight: 400; }
  .header-rule { position: absolute; left: 177px; top: 44px; width: 1023px; height: 12px; }

  .contacts { position: absolute; left: 177px; top: 84px; width: 761px; font-size: 18px; }
  .contacts-label { color: var(--red); font-weight: 700; font-size: 23px; margin-right: 6px; }
  .contacts-line2 { text-align: right; margin-top: 4px; }
  .contacts-line2 b { color: var(--red); font-weight: 700; margin-left: 14px; }

  .series-panel {
    position: absolute; left: 56px; top: 190px; width: 1086px; height: 616px;
    background: var(--panel); border-radius: 0 50px 0 50px;
  }
  .series-title { position: absolute; left: 81px; top: 206px; color: var(--white); font-size: 31px; font-weight: 700; }
  .series-intro {
    position: absolute; left: 81px; top: 256px; width: 1035px;
    font-family: "Ubuntu Condensed", sans-serif; font-size: 14.2px; line-height: 17px; text-align: justify;
  }
  .series-intro p + p { margin-top: 10px; }

  .model { position: absolute; width: 175px; }
  .model-page { font-size: 24px; font-weight: 700; line-height: 1; }
  .model-page span { color: var(--red); }
  .model-control { font-style: italic; font-size: 16px; margin-top: 7px; }
  .model-photo {
    margin-top: 8px; width: 173px; height: 113px;
    border: 1px solid var(--red); border-radius: 0 22px 0 22px;
    background: linear-gradient(180deg, var(--thumb-top), var(--thumb-bottom));
    box-shadow: 4px 5px 7px rgba(0,0,0,0.3);
  }
</style>
</head>
<body>
<div class="page">
  <h1 class="section-title">Contents</h1>
  <svg class="header-rule" viewBox="0 0 1023 12" aria-hidden="true">
    <rect x="1" y="2" width="7" height="7" fill="none" stroke="var(--rule-dark)" stroke-width="1.5"/>
    <line x1="9" y1="4" x2="1023" y2="4" stroke="var(--rule-dark)" stroke-width="2"/>
    <line x1="9" y1="7.5" x2="1023" y2="7.5" stroke="var(--red)" stroke-width="1.5"/>
  </svg>

  <div class="contacts">
    <div><span class="contacts-label">Contacts</span>118-120 Lantern Row, Binh Loi Ward, Dist. 9, Harbor City, Vietnam</div>
    <div class="contacts-line2"><b>T</b> (84) 8-4020-1188 <b>F</b> (84) 8-4020-1190 <b>W</b> www.hoodlineworks.com</div>
  </div>

  <div class="series-panel"></div>
  <h2 class="series-title">RangeHood Series</h2>
  <div class="series-intro">
    <p>An exhaust hood, extractor hood, or range hood is a device containing a mechanical fan that hangs above the stove or cooktop in the kitchen. It removes airborne grease, combustion products, fumes, smoke, odors, heat and steam from the air by evacuation of the air and filtration. In commercial kitchens, exhaust hoods are often used in combination with fire suppression devices so that the fumes from a grease fire are properly vented and the fire is put out quickly. Commercial vent hoods may also be combined with a fresh air fan that draws in exterior air, circulating it with the cooking fumes, which is then drawn out by the hood.</p>
    <p>In most exhaust hoods, a filtration system removes grease (the grease trap) and other particles. Although many vent hoods exhaust air to the outside, some recirculate the air to the kitchen. In a recirculating system, filters may remove odors in addition to the grease.</p>
  </div>

  <div class="model" style="left:82px; top:403px;">
    <div class="model-page">Page <span>01</span></div>
    <div class="model-control">Push Button - 3 Speed</div>
    <div class="model-photo" role="img" aria-label="Stainless steel chimney wall range hood with push button controls"></div>
  </div>
  <div class="model" style="left:297px; top:403px;">
    <div class="model-page">Page <span>02</span></div>
    <div class="model-control">Cap Touch - 4 Speed</div>
    <div class="model-photo" role="img" aria-label="Stainless steel under-cabinet range hood with touch controls"></div>
  </div>
  <div class="model" style="left:512px; top:403px;">
    <div class="model-page">Page <span>03</span></div>
    <div class="model-control">Cap Touch - 4 Speed</div>
    <div class="model-photo" role="img" aria-label="Stainless steel chimney range hood with blue touch display"></div>
  </div>
  <div class="model" style="left:513px; top:604px;">
    <div class="model-page">Page <span>04</span></div>
    <div class="model-control">Cap Touch - 3 Speed</div>
    <div class="model-photo" role="img" aria-label="Slim stainless steel under-cabinet range hood"></div>
  </div>
  <div class="model" style="left:729px; top:604px;">
    <div class="model-page">Page <span>05</span></div>
    <div class="model-control">Push Button - 3 Speed</div>
    <div class="model-photo" role="img" aria-label="Stainless steel chimney range hood with baffle filters"></div>
  </div>
  <div class="model" style="left:945px; top:604px;">
    <div class="model-page">Page <span>06</span></div>
    <div class="model-control">Push Button - 3 Speed</div>
    <div class="model-photo" role="img" aria-label="Stainless steel under-cabinet range hood with push buttons"></div>
  </div>
</div>
</body>
</html>
```